Bellmont Planners, LLC Stationary

Bellmont Planners, LLC is a new financial planning and consulting company. We are looking for designs on business cards, letterhead, envelopes, and anything else that would be useful. Our preference for business card design is two sided. We are looking for a professional and clean look with incorporating the logo and patriotic feel. Thank you to all who participate and good luck!

```html
<!DOCTYPE html>
<html lang="en">
<head>
<meta charset="utf-8">
<title>Bellmont Planners, LLC – Business Card</title>
<link rel="stylesheet" href="https://fonts.googleapis.com/css2?family=Cinzel:wght@400&family=Open+Sans:wght@400;600&display=swap">
<style>
  :root {
    --slate: #4f6475;
    --navy: #0f3e6a;
    --red: #c21f2c;
    --mist: #e6eaef;
    --blush: #f6dfe1;
    --white: #ffffff;
  }
  * { margin: 0; padding: 0; box-sizing: border-box; }
  html, body { width: 1191px; height: 1200px; overflow: hidden; }
  body { background: var(--slate); position: relative; font-family: "Open Sans", sans-serif; }
  .card {
    position: absolute;
    left: 349px;
    width: 488px;
    height: 278px;
    background: var(--white);
  }
  .card--front { top: 247px; }
  .card--back { top: 602px; }
  .card svg { display: block; width: 100%; height: 100%; }
  .brand-name { font-family: "Open Sans", sans-serif; font-weight: 600; fill: var(--navy); }
  .brand-name--small { font-size: 10px; }
  .person-name { font-family: "Cinzel", serif; font-size: 33px; }
  .person-first { fill: var(--navy); }
  .person-last { fill: var(--red); }
  .person-title { font-family: "Open Sans", sans-serif; font-size: 19px; fill: var(--navy); }
  .contact-text { font-family: "Open Sans", sans-serif; font-size: 13px; fill: var(--white); }
  .contact-icon { fill: none; stroke: var(--white); stroke-width: 1.4; }
  .contact-glyph { fill: var(--white); }
</style>
</head>
<body>

<section class="card card--front" aria-label="Business card front">
  <svg viewBox="0 0 542 309" xmlns="http://www.w3.org/2000/svg">
    <polygon points="0,55 330,178 255,309 0,309" fill="var(--mist)"/>
    <line x1="0" y1="43" x2="300" y2="165" stroke="var(--mist)" stroke-width="3"/>
    <polygon points="255,309 272,309 535,138 530,138" fill="var(--blush)"/>
    <circle cx="62" cy="152" r="20" fill="var(--red)"/>
    <text class="brand-name" x="96" y="162" font-size="28">Bellmont Planners, LLC</text>
  </svg>
</section>

<section class="card card--back" aria-label="Business card back">
  <svg viewBox="0 0 542 309" xmlns="http://www.w3.org/2000/svg">
    <polygon points="0,40 402,215 250,309 0,309" fill="var(--navy)"/>
    <line x1="0" y1="54" x2="402" y2="216" stroke="var(--white)" stroke-width="3"/>
    <polygon points="264,309 292,309 542,134 539,134" fill="var(--red)"/>

    <text x="314" y="76" text-anchor="middle" class="person-name"><tspan class="person-first">DANIEL </tspan><tspan class="person-last">HAYES</tspan></text>
    <text x="314" y="105" text-anchor="middle" class="person-title">FINANCIAL PLANNER</text>

    <g class="contact">
      <circle class="contact-icon" cx="41" cy="176" r="11"/>
      <path class="contact-glyph" d="M34,177 L41,170 L48,177 L46,177 L46,182 L36,182 L36,177 Z"/>
      <text class="contact-text" x="66" y="181">Adress</text>
    </g>
    <g class="contact">
      <circle class="contact-icon" cx="41" cy="206" r="11"/>
      <rect class="contact-icon" x="35" y="202" width="12" height="8"/>
      <polyline class="contact-icon" points="35,202 41,207 47,202"/>
      <text class="contact-text" x="66" y="211">DanielHayes@bellmontplanners.com</text>
    </g>
    <g class="contact">
      <circle class="contact-icon" cx="41" cy="236" r="11"/>
      <path class="contact-icon" d="M36,231 Q35,238 44,242 L46,239 L43,237 L41,238 Q38,236 38,234 L40,233 L38,230 Z"/>
      <text class="contact-text" x="66" y="241">(555) 555-0198</text>
    </g>
    <g class="contact">
      <circle class="contact-icon" cx="41" cy="267" r="11"/>
      <circle class="contact-icon" cx="41" cy="267" r="6"/>
      <ellipse class="contact-icon" cx="41" cy="267" rx="2.5" ry="6"/>
      <line class="contact-icon" x1="35" y1="267" x2="47" y2="267"/>
      <text class="contact-text" x="66" y="272">www.bellmontplanners.com</text>
    </g>

    <circle cx="428" cy="273" r="6" fill="var(--navy)"/>
    <text class="brand-name brand-name--small" x="528" y="277" text-anchor="end">Bellmont Planners</text>
  </svg>
</section>

</body>
</html>
```